Elegant Financial Planning Business Card

Clear Harbour Wealth Advisory Pty Ltd requires an elegant business card that communicates simplicity, elegance and trust.
Attached card example of 'Dorvane' is very close to what I am looking for. Looking for black and white card.
Update 24/1/16: The attached Dorvane card is almost exactly what I am looking for. Although it is possible that alternative layouts may interest me, it is considerably more likely that I will proceed with a virtual clone of the "Dorvane' example.
Industry/Entity Type
Financial Planning
Contact Information for Business Card
In black font...
Front Details are (layout as per Paula Dorvane card picture):
Line1 - Name: Simon Walsh
Line 2 - Company: Clear Harbour Wealth Advisory Pty Ltd
Line 3 - Address: Marlow Court 3, Level 14, 58 Tennant Road, Bondi Junction NSW
Line 4
- Phone: 178 526
- Email: advice@chwa-example.com.au
- Site: www.chwa-example.com.au
Back details
1/ logo in position and dimensions as per attached layout
2. Bottom left (in smaller writing).
- Authorised Representative No. 517649
- Clear Harbour Wealth Advisory is a corporate authorised representative of Tidewell Capital Partners Pty Ltd
- ABN 47 318 602 154
- AFSL No. 390817

```html
<!DOCTYPE html>
<html lang="en">
<head>
<meta charset="utf-8">
<title>Clear Harbour Wealth Advisory – Business Card</title>
<link rel="stylesheet" href="https://fonts.googleapis.com/css2?family=EB+Garamond:wght@400;600&display=swap">
<style>
  :root {
    --backdrop: #e9e7e3;
    --divider: #ffffff;
    --card: #f7f7f5;
    --ink: #161616;
    --card-shadow: rgba(0, 0, 0, 0.12);
  }
  * { margin: 0; padding: 0; box-sizing: border-box; }
  html, body {
    width: 1200px;
    height: 2586px;
    overflow: hidden;
    background: var(--backdrop);
  }
  body {
    position: relative;
    font-family: "EB Garamond", "Palatino Linotype", Georgia, serif;
    color: var(--ink);
  }
  .variant {
    position: absolute;
    left: 0;
    width: 1200px;
    height: 1263px;
  }
  .variant--inline { top: 0; }
  .variant--stacked { top: 1323px; }
  .divider {
    position: absolute;
    top: 1263px;
    left: 0;
    width: 1200px;
    height: 60px;
    background: var(--divider);
  }
  .card {
    position: absolute;
    left: 180px;
    width: 840px;
    height: 513px;
    background: var(--card);
    box-shadow: 0 6px 24px var(--card-shadow);
  }
  .card--back { top: 90px; }
  .card--front { top: 660px; }

  /* Back of card */
  .brand {
    position: absolute;
    right: 70px;
    top: 150px;
    display: flex;
    align-items: center;
    gap: 18px;
    font-size: 40px;
    font-weight: 600;
    letter-spacing: 0.5px;
  }
  .brand__square {
    width: 30px;
    height: 30px;
    background: var(--ink);
  }
  .disclosure {
    position: absolute;
    left: 52px;
    bottom: 48px;
    font-size: 17px;
    line-height: 1.35;
  }

  /* Front of card */
  .holder {
    position: absolute;
    left: 56px;
    top: 130px;
  }
  .holder__name {
    font-size: 30px;
    font-weight: 600;
    text-transform: uppercase;
    letter-spacing: 0.5px;
  }
  .holder__company {
    font-size: 24px;
    margin-top: 4px;
  }
  .contact {
    position: absolute;
    left: 56px;
    font-size: 21px;
    line-height: 1.4;
  }
  .variant--inline .contact { top: 350px; }
  .variant--stacked .contact { top: 290px; }
  .contact__sep { padding: 0 10px; }
</style>
</head>
<body>

<section class="variant variant--inline">
  <article class="card card--back">
    <div class="brand"><span class="brand__square"></span>Clear Harbour</div>
    <p class="disclosure">
      Authorised Representative No. 517649<br>
      Clear Harbour Wealth Advisory is a corporate<br>
      authorised representative of Tidewell<br>
      Capital Partners Pty Ltd<br>
      ABN 47 318 602 154 | AFSL No. 390817
    </p>
  </article>
  <article class="card card--front">
    <div class="holder">
      <h1 class="holder__name">Simon Walsh</h1>
      <p class="holder__company">Clear Harbour Wealth Advisory Pty Ltd</p>
    </div>
    <div class="contact">
      <p>Marlow Court 3, Level 14, 58 Tennant Road, Bondi Junction NSW</p>
      <p>Phone: 178 526<span class="contact__sep">|</span>Email: advice@chwa-example.com.au<span class="contact__sep">|</span>Site: www.chwa-example.com.au</p>
    </div>
  </article>
</section>

<div class="divider"></div>

<section class="variant variant--stacked">
  <article class="card card--back">
    <div class="brand"><span class="brand__square"></span>Clear Harbour</div>
    <p class="disclosure">
      Authorised Representative No. 517649<br>
      Clear Harbour Wealth Advisory is a corporate<br>
      authorised representative of Tidewell<br>
      Capital Partners Pty Ltd<br>
      ABN 47 318 602 154 | AFSL No. 390817
    </p>
  </article>
  <article class="card card--front">
    <div class="holder">
      <h2 class="holder__name">Simon Walsh</h2>
      <p class="holder__company">Clear Harbour Wealth Advisory Pty Ltd</p>
    </div>
    <div class="contact">
      <p>Marlow Court 3, Level 14, 58 Tennant Road, Bondi Junction NSW</p>
      <p>Phone: 178 526</p>
      <p>Email: advice@chwa-example.com.au</p>
      <p>Site: www.chwa-example.com.au</p>
    </div>
  </article>
</section>

</body>
</html>
```